Zielgruppe
Steuerberater, Zielgruppe: Mandanten
Aufgabenstellung
Es sollten keine Balken an den Rändern vorhanden sein, so dass das Briefpapier mit dem eigenen Farbdrucker bedruckt werden kann.
-Keine Balken an den Rändern
-Wir wollen kein Briefpapier bedrucken lassen, soll mit dem eigenen Drucker bedruckbar sein
Die Schriftart CG Omega sollte installiert sein, für die korrekte Darstellung.

```html
<!DOCTYPE html>
<html lang="de">
<head>
<meta charset="utf-8">
<title>Briefbogen Kanzlei Velmorix</title>
<link rel="stylesheet" href="https://fonts.googleapis.com/css2?family=Belleza&family=Jost:wght@600&display=swap">
<style>
  :root {
    --navy: #0f2d5c;
    --text-grey: #4a4f55;
    --paper: #ffffff;
    --backdrop: #efefef;
    --rule: #9a9a9a;
  }
  * { margin: 0; padding: 0; box-sizing: border-box; }
  html, body { width: 1200px; height: 1200px; overflow: hidden; background: var(--backdrop); }
  .letterhead {
    position: absolute; left: 206px; top: 42px;
    width: 789px; height: 1115px;
    background: var(--paper);
    border: 1px solid #c8c8c8;
    font-family: "Belleza", "Optima", sans-serif;
    color: var(--text-grey);
  }
  .brand {
    position: absolute; right: 60px; top: 52px; text-align: right;
  }
  .brand-name {
    font-size: 36px; line-height: 1; color: var(--navy); letter-spacing: 0.2px;
  }
  .brand-tagline {
    margin-top: 6px; font-size: 11px; letter-spacing: 1.6px; text-transform: uppercase; color: #3d4a52;
  }
  .fold-mark {
    position: absolute; left: 19px; top: 371px; width: 19px; height: 1px; background: var(--rule);
  }
  .info-block {
    position: absolute; font-size: 11.8px; line-height: 17px;
  }
  .info-block .label {
    font-family: "Jost", "Optima", sans-serif; font-weight: 600; color: var(--navy);
  }
  .sidebar { left: 613px; }
  .footer-col { left: 610px; }
  .tab { display: inline-block; width: 48px; }
</style>
</head>
<body>
  <main class="letterhead">
    <header class="brand">
      <div class="brand-name">Kanzlei Velmorix</div>
      <div class="brand-tagline">Steuerberater &nbsp;|&nbsp; Rechtsanwalt</div>
    </header>

    <div class="fold-mark"></div>

    <section class="info-block sidebar" style="top:170px">
      <div class="label">Tarek Velmorix</div>
      <div>Diplom-Kaufmann</div>
      <div>Steuerberater</div>
    </section>
    <section class="info-block sidebar" style="top:230px">
      <div class="label">Aron Velmorix</div>
      <div>Rechtsanwalt</div>
      <div>Fachanwalt für Steuerrecht</div>
    </section>
    <section class="info-block sidebar" style="top:298px">
      <div>Mühlgasse 14</div>
      <div>71234 Altdorfen</div>
    </section>
    <section class="info-block sidebar" style="top:343px">
      <div><span class="tab">Telefon:</span>07031 – 554210</div>
      <div><span class="tab">Telefax:</span>07031 – 554212</div>
    </section>
    <section class="info-block sidebar" style="top:387px">
      <div>mail@kanzlei-velmorix.de</div>
      <div>www.kanzlei-velmorix.de</div>
    </section>

    <section class="info-block footer-col" style="top:878px">
      <div class="label">Bankverbindung</div>
      <div>Kanzlei Velmorix GbR</div>
      <div>Nordwert Bank AG</div>
    </section>
    <section class="info-block footer-col" style="top:947px">
      <div class="label">IBAN</div>
      <div>DE12 5003 0080 0417 2263 95</div>
    </section>
    <section class="info-block footer-col" style="top:998px">
      <div class="label">BIC</div>
      <div>NRWBDEFFXXX</div>
    </section>
    <section class="info-block footer-col" style="top:1049px">
      <div class="label">Umsatzsteuer-ID</div>
      <div>DE301234567</div>
    </section>
  </main>
</body>
</html>
```